The Brandling Firm

We need a new design for our letterhead and envelopes. We are a personal injury and criminal defense firm so we need something modern and clean, but more on the professional/traditional side. Our new logo has two colors and is attached to the file so we need something that works well with those colors/matches the design. The following information needs to be on the letterhead:
Phone: (555) 314-2716
Fax: (555) 314-5093
Toll-Free: (800) 555-0143
Post Office Box 4372
Lexington, SC 29548-4372
QVHarmCounselGroup.example
MarrowvaleTrialCounsel.example

Target Market(s)

Clients, government agencies, other law firms

Industry/Entity Type

Legal

Font styles to use
Sans Serif
Other font styles liked:
• Arial

Colors

Designer to choose colors to be used in the design.

Requirements
Must have
• Must look professional and clean, modern
Nice to have
• I would like to see a design that works with the logo but does not distract from the content that will be printed on it
Should not have
• Too many colors or crazy designs.

```html
<!DOCTYPE html>
<html lang="en">
<head>
<meta charset="utf-8">
<title>The Brandling Firm – Stationery</title>
<link rel="stylesheet" href="https://fonts.googleapis.com/css2?family=Roboto:wght@400;500&family=Questrial&display=swap">
<style>
  :root {
    --navy: #41449a;
    --navy-deep: #2f3290;
    --red: #d11f26;
    --paper: #f1f1f1;
    --paper-edge: #e6e6e6;
    --ink: #555;
    --ink-dark: #3a3a3a;
    --stage: #e2e2e2;
  }
  * { box-sizing: border-box; margin: 0; padding: 0; }
  html, body { width: 1200px; height: 550px; overflow: hidden; }
  body {
    position: relative;
    background: radial-gradient(ellipse at 50% 40%, #ececec 0%, var(--stage) 70%);
    font-family: "Roboto", Arial, sans-serif;
  }
  .piece { position: absolute; box-shadow: 0 2px 6px rgba(0,0,0,.18); }

  /* Folder */
  .folder {
    left: 42px; top: 34px; width: 384px; height: 488px;
    background: var(--navy);
  }
  .folder-rule {
    position: absolute; top: 0; bottom: 0; width: 1px;
    background: rgba(255,255,255,.35);
  }
  .folder-rule.r1 { left: 10px; }
  .folder-rule.r2 { left: 17px; }
  .folder-rule.r3 { left: 24px; }
  .folder-name {
    position: absolute; left: 0; right: 0; top: 238px;
    text-align: center; color: #fff;
    font: 500 27px "Roboto", Arial, sans-serif; letter-spacing: .5px;
  }
  .folder-urls {
    position: absolute; left: 0; right: 0; top: 442px;
    text-align: center; color: #fff;
    font: 400 6.4px "Roboto", Arial, sans-serif;
  }

  /* Letterhead */
  .letterhead {
    left: 449px; top: 55px; width: 331px; height: 466px;
    background: linear-gradient(90deg, var(--paper) 0%, #f6f6f6 55%, var(--paper-edge) 100%);
  }
  .contact {
    position: absolute; left: 22px; top: 27px;
    font: 400 4.9px/6.3px "Roboto", Arial, sans-serif; color: var(--ink);
  }
  .contact .label { color: var(--navy); font-weight: 500; }
  .contact .gap { height: 3px; }
  .contact .url-a { color: var(--navy); }
  .contact .url-b { color: var(--red); }
  .letterhead-name {
    position: absolute; right: 26px; top: 45px;
    font: 500 11px "Roboto", Arial, sans-serif; color: var(--navy);
  }
  .letter {
    position: absolute; left: 29px; top: 131px; width: 275px;
    font-family: "Questrial", Arial, sans-serif; color: var(--ink);
  }
  .salutation { font-size: 8.6px; margin-bottom: 10px; color: var(--ink-dark); }
  .letter p { font-size: 4.7px; line-height: 6.9px; margin-bottom: 5.5px; text-align: justify; }
  .closing { font-size: 4.8px; margin-top: 12px; }
  .signature {
    width: 58px; height: 22px; margin-top: 10px;
    background: linear-gradient(90deg, rgba(65,68,154,.18), rgba(65,68,154,.06));
    border-radius: 3px;
  }

  /* Envelopes */
  .envelope { width: 334px; background: linear-gradient(90deg, #f5f5f5, #e9e9e9); }
  .envelope-back { left: 828px; top: 133px; height: 151px; }
  .envelope-front { left: 807px; top: 190px; height: 152px; }
  .flap {
    position: absolute; left: 0; right: 0; top: 0;
    border-radius: 0 0 14px 14px;
    display: flex; align-items: center; justify-content: center;
    color: #fff; font: 500 8px "Roboto", Arial, sans-serif; letter-spacing: .3px;
  }
  .flap-red { height: 46px; background: var(--red); }
  .flap-navy { height: 47px; background: var(--navy-deep); }
  .envelope-urls {
    position: absolute; left: 0; right: 0; top: 138px;
    text-align: center; font: 400 5px "Roboto", Arial, sans-serif; color: var(--ink);
  }
  .envelope-small {
    left: 809px; top: 366px; height: 152px;
    background: linear-gradient(90deg, #f7f7f7, #e7e7e7);
  }
  .envelope-name {
    position: absolute; left: 16px; top: 30px;
    font: 500 8.5px "Roboto", Arial, sans-serif; color: var(--navy);
  }
  .envelope-address {
    position: absolute; left: 21px; top: 57px;
    font: 400 4.9px/6.4px "Roboto", Arial, sans-serif; color: var(--ink);
  }
</style>
</head>
<body>

  <section class="piece folder" aria-label="Presentation folder">
    <span class="folder-rule r1"></span>
    <span class="folder-rule r2"></span>
    <span class="folder-rule r3"></span>
    <div class="folder-name">The Brandling Firm</div>
    <div class="folder-urls">www.QVHarmCounselGroup.example | &nbsp;www.MarrowvaleTrialCounsel.example</div>
  </section>

  <section class="piece letterhead" aria-label="Letterhead">
    <div class="contact">
      <div>Post Office Box 4372</div>
      <div>Lexington, SC 29548-4372</div>
      <div class="gap"></div>
      <div><span class="label">Phone :</span> (555) 314-2716</div>
      <div><span class="label">Fax :</span> (555) 314-5093</div>
      <div><span class="label">Toll Free :</span> (800) 555-0143</div>
      <div class="gap"></div>
      <div class="url-a">QVHarmCounselGroup.example</div>
      <div class="url-b">MarrowvaleTrialCounsel.example</div>
    </div>
    <div class="letterhead-name">The Brandling Firm</div>

    <article class="letter">
      <div class="salutation">Dear Mr. Harlow,</div>
      <p>Thank you for reaching out to our office regarding your recent matter. We have reviewed the documents you provided and prepared a summary of the next steps. Please read the enclosed notes carefully and keep them with your records for future reference.</p>
      <p>Our team will contact you within the coming week to schedule a meeting at a time that suits you. During that meeting we will answer your questions and explain the options available in plain terms.</p>
      <p>If any details change before then, please call our office so we can update your file. We value your trust and will work hard to reach a fair outcome on your behalf.</p>
      <p>Thank you again for choosing our firm. We look forward to speaking with you soon.</p>
      <div class="closing">Sincerely,</div>
      <div class="signature" role="img" aria-label="Handwritten signature of Evan Harlow"></div>
    </article>
  </section>

  <section class="piece envelope envelope-back" aria-label="Envelope back with red flap">
    <div class="flap flap-red">The Brandling Firm</div>
  </section>

  <section class="piece envelope envelope-front" aria-label="Envelope back with navy flap">
    <div class="flap flap-navy">The Brandling Firm</div>
    <div class="envelope-urls">www.QVHarmCounselGroup.example | &nbsp;www.MarrowvaleTrialCounsel.example</div>
  </section>

  <section class="piece envelope envelope-small" aria-label="Envelope front">
    <div class="envelope-name">The Brandling Firm</div>
    <div class="envelope-address">
      <div>Post Office Box 4372</div>
      <div>Lexington, SC 29548-4372</div>
    </div>
  </section>

</body>
</html>
```